Vorbanix Stationery Design Project

We need a stationery design for our new business Vorbanix which deals in advanced cleaning technologies such as Ultrasonic cleaning and high pressure cleaning machinery.

Our colour scheme is as per the included files.

We require business cards, letterheads, a brochure folder and email signatures design
Updates

Project Deadline Extended

Apologies for the delay in making a decision on this project. We will be making a final decision during the course of next week

Target Market(s)

Industries ranging from medical, automotive, mining, engineering all requiring specialised cleaning services

Industry/Entity Type

Pressure Cleaning

Requirements
Must have
• Please include our supplied logo and colour scheme. The design needs to be professional but creative.

```html
<!DOCTYPE html>
<html lang="en">
<head>
<meta charset="utf-8">
<title>Vorbanix Stationery Set</title>
<link href="https://fonts.googleapis.com/css2?family=PT+Sans:wght@400;700&family=Tinos&display=swap" rel="stylesheet">
<style>
  :root {
    --ink: #3a393b;
    --blue: #2a57b1;
    --blue-deep: #1b3a8a;
    --blue-title: #2454a6;
    --die-line: #1f6f8a;
    --frame: #a9bfdc;
    --paper: #ffffff;
    --grey-text: #6d6d70;
    --sans: "PT Sans", Arial, sans-serif;
    --serif: "Tinos", "Times New Roman", serif;
  }
  html, body { margin: 0; padding: 0; overflow: hidden; background: #fff; }
  .canvas { position: relative; width: 929px; height: 1200px; overflow: hidden; background: var(--paper); }
  .sheet {
    position: absolute; left: 0; top: 0; width: 1000px; height: 1292px;
    transform: scale(0.929); transform-origin: 0 0;
    font-family: var(--sans); color: var(--ink);
  }
  .shapes { position: absolute; left: 0; top: 0; }
  .abs { position: absolute; margin: 0; }

  .section-title { font-size: 32px; font-weight: 400; color: #111; white-space: nowrap; line-height: 1; }
  .set-title { font-size: 34px; color: var(--blue-title); white-space: nowrap; line-height: 1; }

  .brand { display: flex; align-items: center; gap: 0.35em; white-space: nowrap; }
  .brand .sq { width: 1em; height: 1em; background: var(--blue); flex: none; }
  .brand .name { font-weight: 700; letter-spacing: 0.02em; line-height: 1; }
  .brand .tag { display: block; font-size: 0.34em; font-weight: 400; letter-spacing: 0; margin-top: 0.25em; }
  .brand--light .name { color: #fff; }
  .brand--light .tag { color: #d8d8dc; }
  .brand--light .sq { background: #fff; }
  .brand--dark .name { color: #6a6a6e; }
  .brand--dark .tag { color: #8a8a8e; }

  .contact { font-size: 5.4px; line-height: 1.45; letter-spacing: 0.02em; white-space: nowrap; }
  .contact--light { color: #d4d4d8; }
  .contact--dark { color: var(--grey-text); }
  .contact .gap { display: block; height: 4px; }
  .contact--right { text-align: right; }
  .rule { position: absolute; height: 1px; background: #e8c9cd; }

  .side-label { font-size: 6px; color: #444; white-space: nowrap; }

  .card-name { font-size: 6.5px; color: var(--blue); letter-spacing: 0.03em; text-align: right; white-space: nowrap; line-height: 1.2; }
  .card-role { font-size: 3.6px; color: var(--grey-text); letter-spacing: 0.05em; }
  .web { font-size: 4px; letter-spacing: 0.04em; white-space: nowrap; }

  .letter { font-family: var(--serif); font-size: 5.6px; line-height: 7.2px; color: #222; width: 229px; text-align: justify; }
  .letter p { margin: 0 0 7px; }
  .letter .salute { font-weight: 700; margin-bottom: 10px; }
</style>
</head>
<body>
<div class="canvas">
  <div class="sheet">
    <svg class="shapes" width="1000" height="1292" viewBox="0 0 1000 1292" aria-hidden="true">
      <defs>
        <linearGradient id="blueSweep" x1="0" y1="0" x2="1" y2="1">
          <stop offset="0" stop-color="#3763c0"/>
          <stop offset="1" stop-color="#1b3a8a"/>
        </linearGradient>
        <linearGradient id="cardBack" x1="0" y1="0" x2="1" y2="0">
          <stop offset="0" stop-color="#3562bd"/>
          <stop offset="1" stop-color="#1f3f90"/>
        </linearGradient>
      </defs>

      <!-- outer frame -->
      <rect x="0.5" y="0.5" width="999" height="1291" fill="none" stroke="var(--frame)" stroke-width="1"/>

      <!-- presentation folder -->
      <g class="folder">
        <rect x="49" y="71" width="897" height="501" fill="var(--ink)"/>
        <rect x="297" y="82" width="634" height="455" fill="none" stroke="var(--die-line)" stroke-width="0.8"/>
        <path d="M297 328 C200 270 62 330 63 440 C65 490 85 520 100 537 L297 537" fill="none" stroke="var(--die-line)" stroke-width="0.8"/>
        <path d="M297 537 L310 560 L500 560 L510 537" fill="none" stroke="var(--die-line)" stroke-width="0.8"/>
        <line x1="122" y1="415" x2="155" y2="382" stroke="var(--die-line)" stroke-width="0.8"/>
        <line x1="228" y1="474" x2="262" y2="440" stroke="var(--die-line)" stroke-width="0.8"/>
        <path d="M868 82 L931 82 L931 537 L868 537 Q760 310 868 82 Z" fill="var(--paper)"/>
        <path d="M842 82 Q735 310 842 537 L868 537 Q760 310 868 82 Z" fill="url(#blueSweep)"/>
        <path d="M848 96 Q750 310 848 524" fill="none" stroke="var(--paper)" stroke-width="2.2"/>
      </g>

      <!-- envelope front -->
      <g class="envelope-front">
        <rect x="73.5" y="628.5" width="372" height="177" fill="var(--paper)" stroke="#9a9a9a" stroke-width="1"/>
        <path d="M268 642 L432 642 L432 793 L270 793 Q300 718 268 642 Z" fill="var(--ink)"/>
        <path d="M250 642 Q288 718 254 793 L270 793 Q300 718 268 642 Z" fill="url(#blueSweep)"/>
        <path d="M257 650 Q292 718 260 786" fill="none" stroke="var(--paper)" stroke-width="1.2"/>
      </g>

      <!-- envelope back -->
      <rect x="539.5" y="628.5" width="372" height="177" fill="var(--paper)" stroke="#6d6d6d" stroke-width="1"/>

      <!-- business card front -->
      <g class="card-front">
        <rect x="21" y="852" width="187" height="112" fill="var(--paper)" stroke="#bdbdbd" stroke-width="0.6"/>
        <path d="M21 852 L106 852 Q86 908 106 964 L21 964 Z" fill="var(--ink)"/>
        <path d="M106 852 Q86 908 106 964 L114 964 Q94 908 116 852 Z" fill="url(#blueSweep)"/>
      </g>

      <!-- business card back -->
      <rect x="327" y="852" width="187" height="112" fill="url(#cardBack)"/>

      <!-- letterhead -->
      <g class="letterhead">
        <rect x="616.5" y="878.5" width="309" height="400" fill="var(--paper)" stroke="#9a9a9a" stroke-width="1"/>
        <path d="M617 1200 Q770 1262 925 1212 L925 1278 L617 1278 Z" fill="url(#blueSweep)"/>
        <path d="M617 1222 Q780 1272 925 1226" fill="none" stroke="var(--paper)" stroke-width="2"/>
        <path d="M617 1230 Q780 1282 925 1236 L925 1278 L617 1278 Z" fill="var(--ink)"/>
      </g>
    </svg>

    <!-- section headings -->
    <h2 class="abs section-title" style="left:380px; top:22px;">Folder design</h2>
    <h2 class="abs section-title" style="left:398px; top:584px;">Envelop design</h2>
    <h2 class="abs section-title" style="left:629px; top:834px;">Letter head&nbsp; design</h2>
    <h2 class="abs section-title" style="left:118px; top:984px;">Business card design</h2>
    <h1 class="abs set-title" style="left:64px; top:1157px; font-weight:400;">Complete Stationary Design</h1>

    <!-- folder content -->
    <div class="abs brand brand--light" style="left:389px; top:296px; font-size:18px;">
      <span class="sq"></span>
      <span class="name">VORBANIX<span class="tag">Advanced Cleaning Technologies</span></span>
    </div>
    <div class="abs brand brand--light" style="left:146px; top:420px; font-size:11px;">
      <span class="sq"></span>
      <span class="name">VORBANIX<span class="tag">Advanced Cleaning Technologies</span></span>
    </div>
    <div class="abs contact contact--light" style="left:322px; top:478px;">
      ORTAKENT MAH. LIMAN CADDESI<br>IZMIR / TURKEY
      <span class="gap"></span>
      +225 600 140 22 31<br>+225 600 140 22 48
    </div>
    <div class="abs brand brand--dark" style="left:803px; top:288px; font-size:15px;">
      <span class="sq"></span>
      <span class="name">VORBANIX<span class="tag">Advanced Cleaning Technologies</span></span>
    </div>

    <!-- envelope front content -->
    <div class="abs brand brand--dark" style="left:95px; top:703px; font-size:13px;">
      <span class="sq"></span>
      <span class="name">VORBANIX<span class="tag">Advanced Cleaning Technologies</span></span>
    </div>
    <div class="rule" style="left:99px; top:737px; width:92px;"></div>
    <div class="abs contact contact--dark" style="left:99px; top:741px;">
      ORTAKENT MAH. LIMAN CADDESI<br>IZMIR / TURKEY
    </div>
    <div class="rule" style="left:99px; top:759px; width:92px;"></div>
    <div class="abs contact contact--dark" style="left:99px; top:764px;">
      +225 600 140 22 31<br>+225 600 140 22 48
    </div>
    <span class="abs side-label" style="left:463px; top:706px;">&lt; Front</span>
    <span class="abs side-label" style="left:514px; top:706px;">Back &gt;</span>

    <!-- envelope back content -->
    <div class="abs brand brand--dark" style="left:674px; top:715px; font-size:13px;">
      <span class="sq"></span>
      <span class="name">VORBANIX<span class="tag">Advanced Cleaning Technologies</span></span>
    </div>
    <span class="abs web" style="left:703px; top:767px; color:var(--grey-text);">WWW.VORBANIX.COM</span>

    <!-- business card front content -->
    <div class="abs brand brand--light" style="left:25px; top:897px; font-size:9px;">
      <span class="sq"></span>
      <span class="name">VORBANIX<span class="tag">Advanced Cleaning Technologies</span></span>
    </div>
    <span class="abs web" style="left:37px; top:947px; color:#cfcfd3; font-size:3.6px;">WWW.VORBANIX.COM</span>
    <div class="abs card-name" style="right:811px; top:867px;">
      NADIA KESTREL<br><span class="card-role">GRAPHIC DESIGN</span>
    </div>
    <div class="abs contact contact--dark contact--right" style="right:815px; top:919px; font-size:4.4px;">
      ORTAKENT MAH. LIMAN CADDESI<br>IZMIR / TURKEY
      <span class="gap" style="height:7px;"></span>
      +225 600 140 22 31<br>+225 600 140 22 48
    </div>
    <span class="abs side-label" style="left:212px; top:902px;">&lt; Front</span>
    <span class="abs side-label" style="left:300px; top:902px;">Back &gt;</span>

    <!-- letterhead content -->
    <div class="abs brand brand--dark" style="left:650px; top:902px; font-size:13px;">
      <span class="sq"></span>
      <span class="name">VORBANIX<span class="tag">Advanced Cleaning Technologies</span></span>
    </div>
    <div class="abs letter" style="left:656px; top:954px;">
      <p class="salute">Dear Sir,</p>
      <p>Lorem ipsum dolor sit amet, consectetur adipiscing elit. Quisque tellus lacus, tincidunt nec dignissim id, sollicitudin eu nulla. Mauris venenatis odio a tortor tristique sit amet tincidunt mi mattis. Vestibulum nec ipsum sit amet lectus pellentesque elementum. Proin leo urna, volutpat quis semper commodo, convallis ut tellus. Ut vel tortor erat, ac placerat eros. Suspendisse potenti. Mauris id justo lectus. Nunc ultrices, urna eu rhoncus varius, lacus libero pellentesque nisi, et lobortis nisi nisl eget felis.</p>
      <p>Aliquam feugiat, risus imperdiet interdum aliquet, odio lacus lobortis mauris, ut pretium orci nibh sed risus. Quisque commodo ultricies mi, et vulputate nunc dictum ac. Nullam accumsan, lacus sed cursus auctor, nulla velit pulvinar sem, a eleifend leo ipsum quis ipsum. Cum sociis natoque penatibus et magnis dis parturient montes, nascetur ridiculus mus. Donec nulla ipsum, interdum in interdum vitae, suscipit at leo. Vivamus ac leo non justo vulputate tempor at nec nibh. Nam dui felis, interdum ut tincidunt vitae, venenatis vitae purus.</p>
      <p>Nulla porta metus lorem, in euismod nisi. Suspendisse enim quam, vulputate pharetra imperdiet vel, tempor at elit. Nunc ornare viverra tincidunt. Integer tristique, odio vitae tincidunt dapibus, nulla mi euismod diam, vitae tristique turpis mi volutpat odio. Phasellus placerat velit ut turpis porttitor consequat. Vivamus ut rutrum nunc.</p>
    </div>
    <span class="abs web" style="right:120px; top:1172px; color:var(--grey-text); font-size:3.4px;">WWW.VORBANIX.COM</span>
    <div class="rule" style="left:790px; top:1179px; width:90px;"></div>
    <div class="abs contact contact--dark contact--right" style="right:121px; top:1182px;">
      ORTAKENT MAH. LIMAN CADDESI<br>IZMIR / TURKEY
      <span class="gap"></span>
      +225 600 140 22 31<br>+225 600 140 22 48
    </div>
  </div>
</div>
</body>
</html>
```